TWS Business Card Design

As a full service media and advocacy firm, we lean on years of experience in political and corporate consulting, grassroots campaigning, media placement, and video production to deliver unparalleled results. Recently we have moved into digital media and now provide this service for our clients.

I will add our two company logos to be used on the business cards. The longer logo with "sky reach studio" is our primary logo. Our secondary logo is more square one with "sky reach" and 'digital.media.campaigns" on it. We are looking for clean and modern looking business cards fitting for a digital firm.

I will also add our logos that go well with dark backgrounds.

Industry/Entity Type

Political

Contact Information for Business Card

Denton Pratchard, Director of Campaigns and Digital, 571-482-7165, denton@skyreachstudioco.com, @SkyReachStudioCo, @DentonPratchard, Facebook.com/SkyReachStudioCo

```html
<!DOCTYPE html>
<html lang="en">
<head>
<meta charset="utf-8">
<title>TWS Business Card</title>
<link href="https://fonts.googleapis.com/css2?family=Arimo:wght@400;700&display=swap" rel="stylesheet">
<style>
  :root {
    --backdrop: #6b6d6f;
    --card-white: #f5f5f3;
    --brand-navy: #1f3a8c;
    --brand-sky: #3d8fd0;
    --ink-light: #ffffff;
  }
  html, body {
    margin: 0;
    width: 1200px;
    height: 1000px;
    overflow: hidden;
    background: var(--backdrop);
    font-family: "Arimo", Arial, sans-serif;
  }
  .business-card {
    position: absolute;
    left: 100px;
    top: 214px;
    width: 1000px;
    height: 572px;
    background: var(--card-white);
    overflow: hidden;
    box-shadow: 0 10px 30px rgba(0,0,0,0.35);
  }
  .card-shapes {
    position: absolute;
    inset: 0;
  }
  .brand-name {
    position: absolute;
    top: 62px;
    left: 0;
    width: 100%;
    text-align: center;
    font-size: 82px;
    font-weight: 400;
    letter-spacing: 2px;
    color: var(--brand-sky);
    margin: 0;
  }
  .person {
    position: absolute;
    top: 240px;
    left: 0;
    width: 100%;
    text-align: center;
    color: var(--ink-light);
  }
  .person-name {
    margin: 0;
    font-size: 34px;
    font-weight: 700;
  }
  .person-title {
    margin: 4px 0 0;
    font-size: 28px;
    font-weight: 400;
  }
  .contact-list, .social-list {
    position: absolute;
    list-style: none;
    margin: 0;
    padding: 0;
    color: var(--ink-light);
    font-size: 24px;
    line-height: 34px;
  }
  .contact-list { left: 46px; top: 380px; }
  .social-list { left: 470px; top: 430px; }
  .contact-list li, .social-list li {
    display: flex;
    align-items: center;
    gap: 14px;
  }
  .contact-icon { width: 20px; height: 20px; flex: none; }
  .social-dot {
    width: 12px;
    height: 12px;
    border-radius: 50%;
    background: var(--ink-light);
    flex: none;
    margin: 0 4px;
  }
</style>
</head>
<body>
  <section class="business-card">
    <svg class="card-shapes" width="1000" height="572" viewBox="0 0 1000 572">
      <path d="M0 220 Q 420 150 1000 300 L1000 572 L0 572 Z" fill="var(--brand-navy)"/>
      <path d="M130 178 Q 420 160 760 210" fill="none" stroke="var(--brand-navy)" stroke-width="6"/>
      <path d="M150 295 Q 620 300 900 470 Q 620 318 150 299 Z" fill="var(--brand-sky)"/>
    </svg>

    <h1 class="brand-name">SKY REACH STUDIO</h1>

    <div class="person">
      <p class="person-name">Denton Pratchard</p>
      <p class="person-title">Director of Campaigns and Digital</p>
    </div>

    <ul class="contact-list">
      <li>
        <svg class="contact-icon" viewBox="0 0 20 20"><rect x="5" y="1.5" width="10" height="17" rx="2" fill="none" stroke="#fff" stroke-width="1.6"/><line x1="8.5" y1="15.5" x2="11.5" y2="15.5" stroke="#fff" stroke-width="1.6"/></svg>
        <span>571-482-7165</span>
      </li>
      <li>
        <svg class="contact-icon" viewBox="0 0 20 20"><rect x="1.5" y="4.5" width="17" height="11" fill="none" stroke="#fff" stroke-width="1.6"/><path d="M1.5 4.5 L10 11 L18.5 4.5" fill="none" stroke="#fff" stroke-width="1.6"/></svg>
        <span>denton@skyreachstudioco.com</span>
      </li>
    </ul>

    <ul class="social-list">
      <li><span class="social-dot"></span><span>@SkyReachStudioCo</span></li>
      <li><span class="social-dot"></span><span>@DentonPratchard</span></li>
      <li><span class="social-dot"></span><span>Facebook.com/SkyReachStudioCo</span></li>
    </ul>
  </section>
</body>
</html>
```